Looking for potential sellers

We help people buy and sell homes and are currently looking for potential home sellers. We offer low commissions, are the Local Colorado Springs and Falcon Experts, homes selling fast and at top dollar, Free expert pricing opinions and Consultations, over 9 years of experience, top rated Realtors creative and aggressive marketing strategies. Don't just tour the town, ROAM Kestrelby. phone number 555-013-8842 web roamkestrelby.example

```html
<!DOCTYPE html>
<html lang="en">
<head>
<meta charset="utf-8">
<title>Seller Outreach Postcard – Meadowline Realty</title>
<link href="https://fonts.googleapis.com/css2?family=Montserrat:wght@400;500;700;800&family=Oswald:wght@500&family=Cabin:wght@500;600;700&display=swap" rel="stylesheet">
<style>
  :root{
    --stage:#7a7a7a;
    --ink-dark:#2a2917;
    --panel-dark:#1c1c1c;
    --olive:#a8ac3c;
    --olive-deep:#8f9430;
    --white:#ffffff;
    --paper:#ffffff;
    --stamp:#d4d4d4;
    --rule:#333333;
  }
  *{box-sizing:border-box;margin:0;padding:0}
  html,body{width:1200px;height:1200px;overflow:hidden}
  body{background:var(--stage);position:relative;font-family:"Montserrat",sans-serif}
  .postcard{position:absolute;left:211px;width:759px;height:513px;overflow:hidden;box-shadow:0 2px 6px rgba(0,0,0,.35)}
  .postcard--front{top:78px;background:var(--ink-dark)}
  .postcard--back{top:614px;background:var(--paper)}
  .shapes{position:absolute;inset:0;width:100%;height:100%}

  .headline{position:absolute;left:22px;top:26px;font-weight:800;color:var(--white);font-size:23px;line-height:29px;letter-spacing:.3px}
  .headline__accent{display:block;color:var(--olive);font-size:27px;line-height:36px;margin-top:2px}

  .brand{position:absolute;display:flex;align-items:center;gap:6px;font-family:"Montserrat",sans-serif;font-weight:500}
  .brand__square{width:9px;height:9px;background:var(--olive)}
  .brand--front{right:30px;top:48px;color:var(--white);font-size:17px}
  .brand--back{left:398px;top:44px;color:#222;font-size:13px}

  .portrait{position:absolute;top:330px;width:111px;height:122px;border:3px solid var(--white);border-radius:8px;background:linear-gradient(160deg,#cfcac4,#8c7f74)}
  .portrait--left{left:19px}
  .portrait--right{left:626px}

  .agent{position:absolute;top:404px;color:var(--white);font-size:11px;line-height:14px}
  .agent--left{left:149px}
  .agent--right{right:150px;text-align:right}
  .agent__name{font-weight:700;font-size:13.5px;line-height:16px}
  .agent__role{font-weight:400;letter-spacing:.5px;margin-bottom:4px}
  .agent__phones{font-family:"Cabin",sans-serif;font-weight:500;font-size:10.5px;display:flex;gap:10px;align-items:center}
  .agent--right .agent__phones{justify-content:flex-end}
  .agent__phones svg{width:8px;height:8px;vertical-align:-1px}
  .agent-divider{position:absolute;left:377px;top:407px;width:3px;height:42px;background:var(--ink-dark)}

  .web-front{position:absolute;left:0;right:0;top:472px;text-align:center;color:var(--white);font-size:17px;font-weight:500;letter-spacing:6.5px}

  .tagline{position:absolute;left:22px;top:250px;font-family:"Oswald",sans-serif;font-weight:500;font-size:21px;color:var(--olive);transform:scaleX(.86);transform-origin:left}
  .benefits{position:absolute;left:22px;top:286px;list-style:none;font-family:"Cabin",sans-serif;font-weight:500;color:var(--white);font-size:13.5px}
  .benefits li{display:flex;align-items:center;gap:8px;height:25px}
  .benefits svg{width:9px;height:9px}
  .cta{position:absolute;left:19px;top:394px;width:328px;height:59px;border:1.5px solid var(--olive);border-radius:28px;text-align:center;color:var(--white);font-family:"Cabin",sans-serif}
  .cta__lead{font-weight:700;font-size:12px;margin-top:9px}
  .cta__phone{font-weight:700;font-size:19px;margin-top:2px;display:flex;justify-content:center;align-items:center;gap:6px}
  .cta__phone svg{width:15px;height:15px}
  .web-back{position:absolute;left:59px;top:478px;color:var(--white);font-size:16px;letter-spacing:2.2px;font-weight:400}
  .stamp-box{position:absolute;left:675px;top:20px;width:58px;height:66px;background:var(--stamp)}
  .address-line{position:absolute;left:551px;width:182px;height:1px;background:var(--rule)}
</style>
</head>
<body>

<section class="postcard postcard--front">
  <svg class="shapes" viewBox="0 0 759 513" aria-hidden="true">
    <polygon points="0,238 491,40 759,219 759,394 0,394" fill="var(--olive)"/>
  </svg>
  <svg class="shapes" viewBox="0 0 759 513">
    <polygon role="img" aria-label="Photo of a two-storey craftsman house with landscaped front garden" points="0,252 491,64 759,248 759,394 0,394" fill="url(#frontPhoto)"/>
    <defs>
      <linearGradient id="frontPhoto" x1="0" y1="0" x2="0" y2="1">
        <stop offset="0" stop-color="#9cc3e6"/>
        <stop offset=".45" stop-color="#a9a48f"/>
        <stop offset=".75" stop-color="#4f7a34"/>
        <stop offset="1" stop-color="#5a4638"/>
      </linearGradient>
    </defs>
    <rect x="0" y="394" width="759" height="64" fill="var(--olive)"/>
  </svg>

  <h1 class="headline">ARE YOU CURRENTLY<br>LOOKING FOR POTENTIAL<span class="headline__accent">HOME&nbsp; SELLERS ?</span></h1>

  <div class="brand brand--front"><span class="brand__square"></span>Meadowline Realty</div>

  <div class="portrait portrait--left" role="img" aria-label="Portrait of associate broker Calder Brisk"></div>
  <div class="portrait portrait--right" role="img" aria-label="Portrait of employing broker Ormond Brisk"></div>

  <div class="agent agent--left">
    <p class="agent__name">CALDER BRISK</p>
    <p class="agent__role">ASSOCIATE BROKER</p>
    <p class="agent__phones">
      <span><svg viewBox="0 0 10 10"><circle cx="5" cy="5" r="4.3" fill="none" stroke="#fff" stroke-width="1"/></svg> 555-014-2297</span>
      <span><svg viewBox="0 0 10 10"><circle cx="5" cy="5" r="4.3" fill="none" stroke="#fff" stroke-width="1"/></svg> 555-013-8842(office)</span>
    </p>
  </div>
  <div class="agent-divider"></div>
  <div class="agent agent--right">
    <p class="agent__name">ORMOND BRISK</p>
    <p class="agent__role">EMPLOYING BROKER &amp; OWNER</p>
    <p class="agent__phones">
      <span>555-013-8842(office) <svg viewBox="0 0 10 10"><circle cx="5" cy="5" r="4.3" fill="none" stroke="#fff" stroke-width="1"/></svg></span>
      <span>555-013-8842 <svg viewBox="0 0 10 10"><circle cx="5" cy="5" r="4.3" fill="none" stroke="#fff" stroke-width="1"/></svg></span>
    </p>
  </div>

  <p class="web-front">www.roamkestrelby.example</p>
</section>

<section class="postcard postcard--back">
  <svg class="shapes" viewBox="0 0 759 513">
    <polygon points="317,0 349,0 433,250 385,513 0,513 0,246" fill="var(--olive)"/>
    <polygon role="img" aria-label="Photo of a tan two-storey house with arched porch and flower beds" points="0,0 317,0 428,246 0,246" fill="url(#backPhoto)"/>
    <defs>
      <linearGradient id="backPhoto" x1="0" y1="0" x2="0" y2="1">
        <stop offset="0" stop-color="#dfe3e6"/>
        <stop offset=".4" stop-color="#b5ad6e"/>
        <stop offset=".8" stop-color="#8f8a58"/>
        <stop offset="1" stop-color="#4a7a2c"/>
      </linearGradient>
    </defs>
    <polygon points="0,246 432,246 369,462 0,462" fill="var(--panel-dark)"/>
  </svg>

  <p class="tagline">Don't just tour the town, ROAM Kestrelby.</p>
  <ul class="benefits">
    <li><svg viewBox="0 0 10 10"><path d="M1 5.5 L4 8.5 L9 1.5" fill="none" stroke="var(--olive)" stroke-width="1.8"/></svg>Free expert pricing opinions and Consultations</li>
    <li><svg viewBox="0 0 10 10"><path d="M1 5.5 L4 8.5 L9 1.5" fill="none" stroke="var(--olive)" stroke-width="1.8"/></svg>Over 9 years of experience</li>
    <li><svg viewBox="0 0 10 10"><path d="M1 5.5 L4 8.5 L9 1.5" fill="none" stroke="var(--olive)" stroke-width="1.8"/></svg>Top rated Realtors creative</li>
    <li><svg viewBox="0 0 10 10"><path d="M1 5.5 L4 8.5 L9 1.5" fill="none" stroke="var(--olive)" stroke-width="1.8"/></svg>Aggressive marketing strategies</li>
  </ul>
  <div class="cta">
    <p class="cta__lead">FOR MORE DETAILS PLEASE&nbsp; CALL US TODAY</p>
    <p class="cta__phone"><svg viewBox="0 0 16 16"><circle cx="8" cy="8" r="7" fill="none" stroke="#fff" stroke-width="1.2"/><path d="M5.5 4.5 l1.5 0 l.6 1.8 l-.9.7 a5 5 0 0 0 2.3 2.3 l.7-.9 l1.8.6 l0 1.5 a6 6 0 0 1 -6 -6z" fill="#fff"/></svg>555-013-8842</p>
  </div>
  <p class="web-back">www.roamkestrelby.example</p>

  <div class="brand brand--back"><span class="brand__square"></span>Meadowline Realty</div>
  <div class="stamp-box"></div>
  <div class="address-line" style="top:244px"></div>
  <div class="address-line" style="top:273px"></div>
  <div class="address-line" style="top:302px"></div>
</section>

</body>
</html>
```